Tall Fern Software

We are a software company selling endpoint visibility, access and security technology to enterprise-level IT departments.

Our technology helps organizations gain comprehensive visibility into and control over devices accessing their corporate network so they can quickly identify and address suspicious activity on the network that could lead to potential threats like data breaches.

This technology can cost organizations upwards of $1M - depending on the size of the organization. Our primary clients are Pinnacle 2,000 companies.

We want a professional, polished business card to represent our new brand.

Info fields to include on the card:
Name
Job Title
Office Phone #
Cell Phone #
Email address
Address: 4217 Westbrook Ridge Blvd., Ste. 2600, Bloomington, MN 55918
Website address: www.tallfernsoftware.example
Tagline: See every device. Secure the network.

Logo files and color specs document are attached. Would like color scheme to coordinate with the logo.

Also looking at stationary/envelope designs in conjunction with the business card designs. Received very few designs that included the stationary.

```html
<!DOCTYPE html>
<html lang="en">
<head>
<meta charset="utf-8">
<title>Tall Fern Software — Business Card</title>
<link rel="stylesheet" href="https://fonts.googleapis.com/css2?family=Montserrat:wght@700&family=Open+Sans:wght@400;600;700&display=swap">
<style>
  :root {
    --backdrop: #3b3431;
    --card: #f7f7f6;
    --ink: #111111;
    --ink-soft: #4a4a4a;
    --rule: #3a3a3a;
    --pattern-dark: #1a1a1a;
    --pattern-light: #b9b9b9;
  }
  * { box-sizing: border-box; margin: 0; padding: 0; }
  html, body { width: 1200px; height: 716px; overflow: hidden; }
  body {
    background: var(--backdrop);
    font-family: "Open Sans", Arial, sans-serif;
    color: var(--ink);
    position: relative;
  }
  .card {
    position: absolute;
    top: 210px;
    width: 525px;
    height: 300px;
    background: var(--card);
    overflow: hidden;
  }
  .card--contact { left: 50px; }
  .card--brand { left: 625px; }

  .wordmark {
    font-family: "Montserrat", Arial, sans-serif;
    font-weight: 700;
    color: var(--ink);
    text-transform: uppercase;
    line-height: 1;
  }
  .wordmark__dot {
    display: inline-block;
    border-radius: 50%;
    background: var(--ink);
    vertical-align: middle;
  }

  /* Contact side */
  .card--contact .wordmark {
    position: absolute;
    left: 34px;
    top: 30px;
    display: flex;
    align-items: center;
    gap: 12px;
  }
  .card--contact .wordmark__dot { width: 26px; height: 26px; }
  .card--contact .wordmark__name { font-size: 22px; letter-spacing: 2px; }
  .card--contact .wordmark__sub { display: block; font-size: 12px; letter-spacing: 9px; margin-top: 4px; }

  .person {
    position: absolute;
    left: 34px;
    top: 96px;
    font-size: 15px;
  }
  .person__name { font-weight: 700; }
  .person__title { font-weight: 600; font-size: 12px; border-left: 2px solid var(--ink); padding-left: 6px; margin-left: 4px; }

  .rule { position: absolute; left: 0; width: 100%; height: 1.5px; background: var(--rule); }
  .rule--top { top: 122px; }
  .rule--bottom { top: 258px; }

  .contact-list {
    position: absolute;
    left: 34px;
    top: 134px;
    list-style: none;
    font-size: 11.5px;
    color: var(--ink-soft);
    line-height: 17px;
  }
  .contact-list li { display: flex; align-items: center; gap: 7px; }
  .contact-list svg { width: 10px; height: 10px; fill: var(--ink-soft); flex: none; }

  .address {
    position: absolute;
    right: 28px;
    top: 196px;
    text-align: right;
    font-size: 11.5px;
    font-style: normal;
    line-height: 17px;
    color: var(--ink-soft);
  }

  .pattern-area {
    position: absolute;
    right: 0;
    top: 40px;
    width: 120px;
    height: 90px;
    background: linear-gradient(90deg, var(--pattern-light), var(--pattern-dark));
    border-radius: 45px 0 0 45px;
    opacity: .85;
  }

  /* Brand side */
  .card--brand .wordmark {
    position: absolute;
    left: 54px;
    top: 92px;
  }
  .card--brand .wordmark__name { font-size: 44px; letter-spacing: 3px; }
  .card--brand .wordmark__sub { display: block; font-size: 20px; letter-spacing: 16px; margin-top: 4px; }
  .tagline {
    position: absolute;
    left: 56px;
    top: 172px;
    font-size: 13px;
    font-weight: 600;
    letter-spacing: 1.6px;
    color: var(--ink);
  }
  .card--brand .pattern-area {
    top: 60px;
    width: 150px;
    height: 200px;
    border-radius: 100px 0 0 100px;
    background: linear-gradient(90deg, #e4e4e4, var(--pattern-dark));
  }
</style>
</head>
<body>

  <section class="card card--contact" aria-label="Business card, contact side">
    <div class="wordmark">
      <span class="wordmark__dot"></span>
      <span><span class="wordmark__name">Tall Fern</span><span class="wordmark__sub">Software</span></span>
    </div>

    <div class="pattern-area" role="img" aria-label="Decorative dot pattern"></div>

    <p class="person"><span class="person__name">Daniel Hart</span><span class="person__title">Director</span></p>
    <div class="rule rule--top"></div>

    <ul class="contact-list">
      <li><svg viewBox="0 0 10 10"><path d="M2 0h2l1 3-1.5 1a6 6 0 0 0 2.5 2.5L7 5l3 1v2c0 1-1 2-2 2A8 8 0 0 1 0 2C0 1 1 0 2 0z"/></svg>+1 612 555 0148</li>
      <li><svg viewBox="0 0 10 10"><path d="M3 0h4a1 1 0 0 1 1 1v8a1 1 0 0 1-1 1H3a1 1 0 0 1-1-1V1a1 1 0 0 1 1-1zm0 1.5v6h4v-6z"/></svg>+1 612 555 0148</li>
      <li><svg viewBox="0 0 10 10"><path d="M0 2h10v6H0zm1 1v.3l4 2.5 4-2.5V3z"/></svg>info@tallfernsoftware.example</li>
      <li><svg viewBox="0 0 10 10"><path d="M5 0a5 5 0 1 0 0 10A5 5 0 0 0 5 0zm0 1.2c.6.6 1 1.8 1.1 3.2H3.9C4 3 4.4 1.8 5 1.2zM1.2 5.6h1.5c0 1 .2 2 .6 2.8a3.9 3.9 0 0 1-2.1-2.8zm0-1.2a3.9 3.9 0 0 1 2.1-2.8c-.4.8-.6 1.8-.6 2.8zm2.7 1.2h2.2C6 7 5.6 8.2 5 8.8 4.4 8.2 4 7 3.9 5.6zm2.8 2.8c.4-.8.6-1.8.6-2.8h1.5a3.9 3.9 0 0 1-2.1 2.8zm.6-4c0-1-.2-2-.6-2.8a3.9 3.9 0 0 1 2.1 2.8z"/></svg>www.tallfernsoftware.example</li>
    </ul>

    <address class="address">
      4217 Westbrook Ridge Blvd.,<br>
      Ste. 2600, Bloomington,<br>
      MN 55918
    </address>
    <div class="rule rule--bottom"></div>
  </section>

  <section class="card card--brand" aria-label="Business card, brand side">
    <div class="wordmark">
      <span class="wordmark__name">Tall Fern</span>
      <span class="wordmark__sub">Software</span>
    </div>
    <p class="tagline">See every device. Secure the network.</p>
    <div class="pattern-area" role="img" aria-label="Decorative dot pattern"></div>
  </section>

</body>
</html>
```